Health care technology software systems

We have a solid logo. We have company colors that will need to be used as well. We just need a great business card design. We sell to health plans but want to be modern
Updates

Need extra days to review

Target Market(s)

Health technology sector selling into Health Plans

Industry/Entity Type

Health Care Technology

Contact Information for Business Card

Name, title, address, phone number, email

Requirements
Must have
• Use of Kembrata corporate colors - Uploaded w/ our logos

```html
<!DOCTYPE html>
<html lang="en">
<head>
<meta charset="utf-8">
<title>Kembrata Business Card</title>
<link href="https://fonts.googleapis.com/css2?family=Open+Sans:wght@300;400;700&display=swap" rel="stylesheet">
<style>
  :root {
    --bg: #e9eaec;
    --card: #ffffff;
    --ink: #3a3a3c;
    --royal: #3a5ba9;
    --royal-deep: #33519b;
    --sky: #1ea3dc;
    --leaf: #7dbb32;
    --white: #ffffff;
  }
  * { box-sizing: border-box; margin: 0; padding: 0; }
  html, body { width: 1200px; height: 900px; overflow: hidden; }
  body {
    background: var(--bg);
    font-family: "Open Sans", Arial, sans-serif;
    display: flex; flex-direction: column; align-items: center; justify-content: center;
    gap: 50px;
  }
  .card {
    position: relative;
    width: 630px; height: 360px;
    background: var(--card);
    box-shadow: 0 8px 24px rgba(0,0,0,0.18);
    overflow: hidden;
  }
  .brand { display: flex; align-items: center; gap: 16px; }
  .brand-dot { width: 30px; height: 30px; border-radius: 50%; background: var(--royal); }
  .brand-name { font-weight: 300; color: var(--ink); letter-spacing: 1px; line-height: 1; }
  .card-front .brand { position: absolute; left: 50%; top: 50%; transform: translate(-50%, -50%); }
  .card-front .brand-name { font-size: 64px; }
  .card-back .brand { position: absolute; left: 40px; top: 48px; }
  .card-back .brand-name { font-size: 56px; }
  .info-band {
    position: absolute; left: 0; right: 0; bottom: 0; height: 146px;
    background: linear-gradient(90deg, var(--royal-deep), var(--royal));
  }
  .identity { position: absolute; left: 44px; top: 238px; font-size: 17px; color: var(--leaf); }
  .identity .person { font-weight: 700; text-transform: uppercase; letter-spacing: 0.5px; }
  .identity .role { font-weight: 400; border-left: 2px solid var(--white); padding-left: 6px; margin-left: 4px; }
  .contacts { position: absolute; left: 44px; top: 274px; list-style: none; color: var(--white); font-size: 15px; line-height: 24px; }
  .contacts li { display: flex; align-items: center; gap: 8px; }
  .contacts svg { width: 12px; height: 12px; fill: var(--sky); }
  .divider { position: absolute; left: 262px; top: 250px; width: 2px; height: 80px; background: var(--white); opacity: 0.8; }
  .address { position: absolute; left: 286px; top: 244px; display: flex; gap: 10px; color: var(--white); font-size: 15px; line-height: 22px; }
  .address svg { width: 14px; height: 18px; fill: var(--sky); margin-top: 2px; }
</style>
</head>
<body>
  <section class="card card-front">
    <div class="brand"><span class="brand-dot"></span><span class="brand-name">Kembrata</span></div>
  </section>

  <section class="card card-back">
    <div class="info-band" role="img" aria-label="Decorative brand-colour wave area"></div>
    <div class="brand"><span class="brand-dot"></span><span class="brand-name">Kembrata</span></div>
    <p class="identity"><span class="person">Daniel Okoro</span><span class="role">Director</span></p>
    <ul class="contacts">
      <li><svg viewBox="0 0 12 12"><path d="M2 1h3l1 3-2 1a7 7 0 0 0 3 3l1-2 3 1v3c-6 0-9-3-9-9z"/></svg>0912 480 375</li>
      <li><svg viewBox="0 0 12 12"><path d="M0 2h12v8H0z M0 2l6 5 6-5"/></svg>info@kembrata.com</li>
      <li><svg viewBox="0 0 12 12"><circle cx="6" cy="6" r="6"/></svg>www.kembrata.com</li>
    </ul>
    <span class="divider"></span>
    <div class="address">
      <svg viewBox="0 0 14 18"><path d="M7 0a7 7 0 0 0-7 7c0 5 7 11 7 11s7-6 7-11a7 7 0 0 0-7-7zm0 10a3 3 0 1 1 0-6 3 3 0 0 1 0 6z"/></svg>
      <p>24 Harbor Row, Eastgate<br>P.O Box 4410 Northvale</p>
    </div>
  </section>
</body>
</html>
```